salami paper bag design The size is 10.5cm 21.5cm 6.7cm

This time we need to make renew salami package design. Planning to make paper salami package. I tried to design but I couldnt formyself.
So please correct my design and recreate more nicer package design from my salami design that attach on the documents.
Logo part I am planning gold stamp. If anybody can make more nicer logo for the package,I don’t mind it.please change the color and shape and everything.
The size is 10.5cm 21.5cm 6.7cm
Thank you.

Target Market(s)

uper market make costomer feel luxurious

Industry/Entity Type

salami matured meat products

Font styles to use
Sans Serif
Decorative
Script

Colors

Designer to choose colors to be used in the design.

Requirements
Nice to have
• Make customer feel joy for genuine fermented salami with wine
Should not have
• My projrct must not have cheap discount design.

```html
<!DOCTYPE html>
<html lang="ja">
<head>
<meta charset="utf-8">
<title>自家製熟成生サラミ — 背面パッケージ</title>
<link rel="stylesheet" href="https://fonts.googleapis.com/css2?family=Noto+Sans+JP:wght@400;500&display=swap">
<style>
  :root {
    --backdrop: #f4f4f4;
    --silver-dark: #c4c4c4;
    --silver-light: #ffffff;
    --ink: #1c1c1c;
    --gold: #c9a34a;
    --gold-deep: #a8822e;
    --wine: #b3141b;
    --wine-deep: #650a0e;
    --label-fill: #f4f8dc;
    --label-ink: #8a8a7a;
  }
  html, body {
    margin: 0;
    width: 1200px;
    height: 960px;
    overflow: hidden;
    background: var(--backdrop);
    font-family: "Noto Sans JP", sans-serif;
    color: var(--ink);
  }
  .back-panel {
    position: absolute;
    left: 370px;
    top: 10px;
    width: 460px;
    height: 940px;
    overflow: hidden;
    background: var(--silver-light);
  }
  .pattern-field {
    position: absolute;
    inset: 0 0 auto 0;
    height: 780px;
    background: linear-gradient(to bottom, var(--silver-dark) 0%, #dcdcdc 35%, #f1f1f1 70%, var(--silver-light) 100%);
  }
  .wine-band {
    position: absolute;
    left: 0; right: 0; bottom: 0;
    height: 160px;
    background: linear-gradient(to bottom, var(--wine) 0%, #8e1016 55%, var(--wine-deep) 100%);
  }
  .awards {
    position: absolute;
    top: 285px;
    left: 24px;
    right: 20px;
    display: flex;
    align-items: center;
    gap: 10px;
  }
  .award-seal {
    width: 40px;
    height: 46px;
    background: linear-gradient(135deg, #e3c67a, var(--gold-deep));
    border-radius: 6px 6px 20px 20px;
    flex: none;
  }
  .award-seal.round {
    width: 44px;
    height: 44px;
    border-radius: 50%;
  }
  .awards-text { margin-left: 6px; }
  .awards-head { font-size: 15px; margin: 0 0 6px; font-weight: 400; }
  .awards-line { font-size: 10.5px; margin: 0; line-height: 1.45; }
  .section-title {
    position: absolute;
    left: 0; right: 0;
    text-align: center;
    font-size: 17px;
    font-weight: 400;
    margin: 0;
  }
  .title-main { top: 368px; }
  .title-serve { top: 632px; }
  .story {
    position: absolute;
    top: 408px;
    left: 28px;
    right: 24px;
    font-size: 9.6px;
    line-height: 15px;
  }
  .story p { margin: 0 0 10px; }
  .serving {
    position: absolute;
    top: 672px;
    left: 28px;
    right: 20px;
    list-style: none;
    margin: 0; padding: 0;
    font-size: 9.6px;
    line-height: 14px;
  }
  .serving li {
    display: flex;
    gap: 8px;
    align-items: flex-start;
    margin-bottom: 8px;
  }
  .bullet-ornament {
    flex: none;
    width: 32px;
    height: 10px;
    margin-top: 2px;
    border-radius: 5px;
    background: linear-gradient(90deg, #e3c67a, var(--gold));
  }
  .label-space {
    position: absolute;
    left: 80px;
    top: 752px;
    width: 300px;
    height: 170px;
    background: var(--label-fill);
    border: 1.5px solid #1c1c1c;
    border-radius: 16px;
    display: flex;
    flex-direction: column;
    align-items: center;
    justify-content: center;
    gap: 6px;
    font-size: 9px;
    color: var(--label-ink);
  }
</style>
</head>
<body>
  <main class="back-panel">
    <div class="pattern-field" role="img" aria-label="淡いシルバーの花柄地紋"></div>
    <div class="wine-band" role="img" aria-label="ワインレッドの花柄地紋の帯"></div>

    <section class="awards">
      <div class="award-seal" role="img" aria-label="受賞バッジ"></div>
      <div class="award-seal round" role="img" aria-label="金賞バッジ"></div>
      <div class="awards-text">
        <p class="awards-head">受賞するのは最高の食品だけ</p>
        <p class="awards-line">ILQドイツ国際品質競技会金賞受賞</p>
        <p class="awards-line">食の逸品コンクール美食審査会100選受賞</p>
      </div>
    </section>

    <h1 class="section-title title-main">自家製熟成生サラミ</h1>

    <article class="story">
      <p>当店の造る生サラミ（発酵サラミ）は、スローフード食品です。生サラミや生ハムにはビタミンB群やタンパク質等の良質な栄養成分が豊富に含まれています。当店の生サラミ、生ハムの絶品の秘密は、毎日市場から仕入れる新鮮で豚枝格付け「上物」のみを使用していること、そしてドイツ産岩塩ベルクザルツ、ミネラル豊富なフランスの100%オーガニック「ラ・サリーヌ・ブランシュ」等の厳選した調味料を使用していることにあります。</p>
      <p>生サラミや生ハムは時間をかけてゆっくり熟成していく過程で、製品内のタンパク質分解され必須アミノ酸になり、完成までに元のアミン酸の数倍になります。</p>
      <p>この生ハム生サラミに含まれるアミノ酸はコラーゲンの原料となり、美肌を作る役割を果たす他、血液の流れを良くして基礎代謝を上げる効果を持つといわれています。</p>
    </article>

    <h2 class="section-title title-serve">美味しいお召し上がり方法</h2>

    <ul class="serving">
      <li><span class="bullet-ornament" role="img" aria-label="金色の飾り"></span>そのまま薄くスライスしてお楽しみいただけます。</li>
      <li><span class="bullet-ornament" role="img" aria-label="金色の飾り"></span>温野菜などを添えクラッカーと一緒に。</li>
      <li><span class="bullet-ornament" role="img" aria-label="金色の飾り"></span>クリームチーズを添えて。なめらかな香りが素材本来の風味を際立たせます。もちろんお酒のつまみとしても絶品です。</li>
    </ul>

    <div class="label-space">
      <span>Labeling space</span>
      <span>ラベル貼付けガイド</span>
      <span>W60×H95</span>
    </div>
  </main>
</body>
</html>
```